Tovesca Website

I need a website for a startup company that provides GIS (Geographic Information Services) staffing and products for local cities. Current website is www.tovescagroup.com

```html
<!DOCTYPE html>
<html lang="en">
<head>
<meta charset="utf-8">
<title>Tovesca Group</title>
<link rel="stylesheet" href="https://fonts.googleapis.com/css2?family=Plus+Jakarta+Sans:wght@500;600;700&family=Mulish:wght@400&display=swap">
<style>
:root{
  --brand-blue:#002a96;
  --ink:#000;
  --muted:#7a7a7a;
  --line:#bdbdbd;
  --footer-bg:#f4f4f4;
  --white:#fff;
}
*{margin:0;padding:0;box-sizing:border-box}
html,body{width:689px;height:1200px;overflow:hidden;background:var(--white)}
body{position:relative;font-family:"Plus Jakarta Sans",sans-serif;color:var(--ink)}
.abs{position:absolute}
.center-x{left:0;width:689px;text-align:center}

.brand-name{left:64px;top:26px;font-weight:700;font-size:11px;color:var(--brand-blue);letter-spacing:-.2px}
.nav-link{top:27px;font-weight:600;font-size:9.5px;color:var(--muted);letter-spacing:-.2px}
.nav-link.active{color:var(--brand-blue);border-bottom:1.2px solid var(--brand-blue);padding-bottom:1px}
.btn{display:flex;align-items:center;justify-content:center;background:var(--brand-blue);color:var(--white);font-weight:700;font-size:7.6px;border-radius:3px;letter-spacing:-.1px}

.hero-title{top:106px;font-weight:600;font-size:29px;line-height:30px;letter-spacing:-1px}
.hero-title .company{color:var(--brand-blue)}
.hero-copy{top:175px;font-family:"Mulish",sans-serif;font-size:6.6px;line-height:9.4px}

.band{left:0;width:689px;height:21px;background:var(--ink);color:var(--white);font-weight:600;font-size:12.3px;display:flex;align-items:center;justify-content:center;letter-spacing:-.3px}

.service-title{top:342px;width:200px;text-align:center;color:var(--brand-blue);font-weight:600;font-size:13px;letter-spacing:-.4px}
.service-box{top:373px;width:169px;height:169px;border:0.7px solid #333;border-radius:38px;padding:22px 0 0 32px}
.service-list{list-style:disc;font-weight:500;font-size:12.3px;line-height:18px;letter-spacing:-.35px}

.form-heading{top:664px;color:var(--brand-blue);font-weight:600;font-size:13px;letter-spacing:-.4px}
.field{left:186px;width:317px;border-bottom:0.7px solid var(--line)}
.field-label{position:absolute;left:12px;font-weight:500;font-size:11.4px;color:var(--muted);letter-spacing:-.3px}

.footer{left:0;top:1001px;width:689px;height:199px;background:var(--footer-bg)}
.footer-brand{top:1037px;font-weight:700;font-size:11px;color:var(--brand-blue)}
.footer-text{font-family:"Mulish",sans-serif;font-size:8.5px;line-height:12.3px}
</style>
</head>
<body>
<header>
  <div class="abs brand-name">Tovesca</div>
  <nav>
    <a class="abs nav-link active" style="left:281px">Home</a>
    <a class="abs nav-link" style="left:349px">Our services</a>
  </nav>
  <a class="abs btn" style="left:570px;top:23px;width:53px;height:21px">Contact Us</a>
</header>

<section>
  <h1 class="abs center-x hero-title"><span class="company">Tovesca Group</span><br>We Make GIS Work For You</h1>
  <p class="abs center-x hero-copy">We are an innovative team of geospatial experts with 25 years of experience in the field of GIS.<br>We specialize in providing results-driven GIS solutions<br>for local government and the private sector.</p>
</section>

<section>
  <h2 class="abs band" style="top:284px">Our services</h2>

  <h3 class="abs service-title" style="left:47px">GIS Consulting</h3>
  <div class="abs service-box" style="left:62px">
    <ul class="service-list">
      <li>GIS projects</li>
      <li>Staffing solutions</li>
      <li>System architecture<br>design</li>
      <li>GIS analysis</li>
      <li>Demographics</li>
      <li>Map products</li>
    </ul>
  </div>

  <h3 class="abs service-title" style="left:244px">GIS Applications</h3>
  <div class="abs service-box" style="left:260px">
    <ul class="service-list">
      <li>Atlasly Online</li>
      <li>Atlasly Enterprise</li>
      <li>Dashboards</li>
      <li>Atlasly Builder</li>
      <li>Custom widgets</li>
      <li>Custom JavaScript<br>apps</li>
    </ul>
  </div>

  <h3 class="abs service-title" style="left:442px">Spatial Data Solutions</h3>
  <div class="abs service-box" style="left:458px">
    <ul class="service-list">
      <li>Spatial data cleanup</li>
      <li>GIS data model<br>design/review</li>
      <li>Integrating with other<br>systems</li>
    </ul>
  </div>
</section>

<section>
  <h2 class="abs band" style="top:601px">Contact Us</h2>
  <h3 class="abs center-x form-heading">Interested in learning more?</h3>
  <div class="abs field" style="top:722px;height:20px"><span class="field-label" style="top:1px">Full name *</span></div>
  <div class="abs field" style="top:757px;height:20px"><span class="field-label" style="top:1px">Email *</span></div>
  <div class="abs field" style="top:792px;height:20px"><span class="field-label" style="top:1px">Phone</span></div>
  <div class="abs field" style="top:825px;height:85px"><span class="field-label" style="top:8px">Message *</span></div>
  <a class="abs btn" style="left:197px;top:932px;width:41px;height:20px">Send</a>
</section>

<footer>
  <div class="abs footer"></div>
  <div class="abs center-x footer-brand">Tovesca</div>
  <p class="abs center-x footer-text" style="top:1062px">Tovesca Group, LLC</p>
  <a class="abs btn" style="left:318px;top:1097px;width:53px;height:20px">Contact Us</a>
  <p class="abs center-x footer-text" style="top:1140px">4185 W. Harlow Ave. #2207<br>Brookdale, CA 92761</p>
</footer>
</body>
</html>
```